Website for company called VELQUOgen

We need a website for our new company called VELQUOgen which developed a platform/technology to identify antigen-specific T cells (immune cells) which can be used for cancer therapy, autoimmunity, etc.

The platform is called VELQUO and is rapid, versatile, unbiased, and inexpensive.

We have a semi-final logo although we are not completely set on color and font of text (attached).

Target Market(s)

Our target audience at the moment would be potential investors and VCs. We eventually are interested in getting attention from scientists and cell/immunotherapy companies.

Industry/Entity Type

Healthcare/Technology

Coding

Coded - Design and coding required

Number of Pages Required

1 page

Colors
0094D4
00A9DD
6FCCEA
C7EBF8
E9F6FB
00AB8E
00BBA5
67D7C9
C6EFE9
E9F9F6
E54698
E96AAD
F1A4CE
F9D9EA
FCEFF6
A7469A
B969AE
D3A5CF
EDDBEB
F8F0F9
6B429C
8869AF
B7A5CE
E3DAEB
F3F0F8

Requirements
Must have
• Landing page about the company, About us page, Technology page (could be merged with company landing page), Contact us page

```html
<!DOCTYPE html>
<html lang="en">
<head>
<meta charset="utf-8">
<title>VELQUOgen — Precision Immune Targeting</title>
<link rel="stylesheet" href="https://fonts.googleapis.com/css2?family=Sora:wght@400;500;600;700;800&family=Poppins:wght@400;500&display=swap">
<style>
:root{
  --purple:#6b429c;
  --purple-btn:#7442a0;
  --purple-mid:#8869af;
  --purple-soft:#b7a5ce;
  --lilac:#e3daeb;
  --lilac-pale:#f3f0f8;
  --ink:#111111;
  --text:#2b2b2b;
  --muted:#555;
  --dark:#050505;
  --band:#7a4aa9;
  --footer:#e6ddef;
}
*{margin:0;padding:0;box-sizing:border-box}
html,body{width:1200px;height:3685px;overflow:hidden}
body{font-family:"Poppins",sans-serif;color:var(--text);background:#fff;position:relative}
.abs{position:absolute}
h1,h2,h3,.display{font-family:"Sora",sans-serif;font-weight:500;color:var(--ink)}

/* header */
.site-header{position:absolute;left:0;top:0;width:1200px;height:80px;background:var(--lilac-pale);border-bottom:1px solid #ddd3e6;z-index:2}
.brand{position:absolute;font-family:"Sora",sans-serif;font-weight:600;color:var(--ink);display:flex;align-items:center;gap:10px}
.brand .dot{width:18px;height:18px;border-radius:50%;background:var(--ink)}
.site-header .brand{left:89px;top:24px;font-size:26px}
.main-nav{position:absolute;left:628px;top:31px;display:flex;gap:28px;font-size:13px;color:var(--ink);align-items:center}
.main-nav .home{width:14px;height:14px}
.pill{position:absolute;display:flex;align-items:center}
.pill span{background:var(--purple-btn);color:#fff;font-family:"Sora",sans-serif;font-weight:500;font-size:13px;border-radius:30px;display:flex;align-items:center;justify-content:center;height:100%}
.pill i{position:absolute;right:0;top:0;border-radius:50%;background:var(--purple-btn);border:2px solid #fff;display:flex;align-items:center;justify-content:center}

/* hero */
.hero{position:absolute;left:0;top:80px;width:1200px;height:617px;background:linear-gradient(160deg,#f4eef7 0%,#ece3f1 55%,#e9ddf0 100%);border-bottom:1px solid #ddd}
.hero h1{position:absolute;left:113px;top:160px;font-size:47px;line-height:54px;letter-spacing:-.5px}
.hero p{position:absolute;left:113px;top:293px;font-size:15.5px;line-height:23px;width:560px}
.hero-art{position:absolute;left:735px;top:82px;width:355px;height:452px;border-radius:48%;background:radial-gradient(circle at 50% 45%,#6fcdea 0%,#2c6fb0 45%,rgba(107,66,156,.25) 75%,rgba(243,240,248,0) 100%)}

/* intro */
.intro{position:absolute;left:0;top:697px;width:1200px;height:988px;background:linear-gradient(180deg,#f6f2f9 0%,#fff 35%,#f9f6fb 70%,#f1e9f5 100%)}
.intro .plate{position:absolute;left:150px;top:290px;width:176px;height:190px;background:#d6c5e2;border-radius:0 0 0 30px}
.intro .photo{position:absolute;left:172px;top:111px;width:317px;height:346px;border-radius:24px;background:linear-gradient(135deg,#0d3f86 0%,#2f8fc8 50%,#8fe1f2 100%)}
.intro .intro-title{position:absolute;left:546px;top:170px;font-size:33px}
.intro .intro-text{position:absolute;left:546px;top:234px;width:490px;font-size:15.5px;line-height:23px}
.intro .how-title{position:absolute;left:0;width:1200px;text-align:center;top:545px;font-size:34px}
.step-label{position:absolute;width:240px;text-align:center;font-family:"Sora",sans-serif;font-size:20px;color:var(--ink)}
.step-label small{display:block;font-family:"Poppins",sans-serif;font-size:14px;color:var(--muted);line-height:20px;margin-top:4px}

/* about */
.about{position:absolute;left:0;top:1685px;width:1200px;height:641px;background:radial-gradient(ellipse at 30% 30%,#141414 0%,var(--dark) 70%);color:#fff}
.about .tag{position:absolute;left:52px;top:150px;transform:rotate(-70deg);font-family:"Sora",sans-serif;color:var(--purple-mid);font-size:20px}
.about h2{position:absolute;left:89px;top:140px;font-size:64px;font-weight:800;color:#fff;letter-spacing:-1px}
.about p.lead{position:absolute;left:89px;top:238px;width:560px;font-size:16.5px;line-height:23px}
.about h3{position:absolute;font-size:20px;color:#8c5cc4;font-weight:500}
.about .mission{position:absolute;left:89px;top:394px;width:300px;font-size:15.5px;line-height:23px}
.values{position:absolute;left:426px;top:392px;list-style:none;font-size:15.5px;line-height:26.5px}
.values li::before{content:"";display:inline-block;width:5px;height:5px;border-radius:50%;background:var(--purple-mid);margin-right:9px;vertical-align:middle}
.about .photo{position:absolute;left:734px;top:118px;width:376px;height:407px;border-radius:20px;background:linear-gradient(160deg,#5f8fb8 0%,#c9d8e6 45%,#3d6fb5 75%,#222 100%)}

/* why */
.why{position:absolute;left:0;top:2326px;width:1200px;height:824px;background:linear-gradient(180deg,#fff 0%,#f6f2f9 100%)}
.why h2{position:absolute;left:0;width:1200px;text-align:center;top:90px;font-size:35px}
.row{position:absolute;left:127px;width:945px;height:146px}
.row.active{background:var(--purple-btn);border-radius:22px;color:#fff}
.row .mark{position:absolute;left:48px;top:50%;width:60px;height:60px;margin-top:-30px;border-radius:50%;background:var(--ink)}
.row.active .mark{background:#fff}
.row h3{position:absolute;left:173px;top:44px;font-size:20px;font-weight:500}
.row.active h3{color:#fff}
.row .sub{position:absolute;left:173px;top:74px;font-size:14px;line-height:20px;width:190px;color:var(--muted)}
.row.active .sub{color:#eee}
.row .desc{position:absolute;left:395px;top:41px;width:380px;font-size:14px;line-height:22px;color:var(--muted)}
.row.active .desc{color:#f0eaf6}
.row .go{position:absolute;left:829px;top:50%;margin-top:-35px;width:70px;height:70px;border-radius:50%;background:var(--ink);display:flex;align-items:center;justify-content:center}
.row.active .go{background:#fff}
.divider{position:absolute;left:127px;width:945px;height:1px;background:#c9c2cf}

/* connect */
.connect{position:absolute;left:0;top:3150px;width:1200px;height:255px;background:linear-gradient(90deg,#7446a6 0%,#7b4aa9 60%,#8a5cb6 100%);overflow:hidden}
.connect h2{position:absolute;left:89px;top:82px;font-size:66px;font-weight:800;color:#fff;letter-spacing:-1px}
.connect p{position:absolute;left:91px;top:163px;font-size:19px;color:#f0e8f7}
.connect .glow{position:absolute;left:780px;top:20px;width:360px;height:300px;border-radius:50%;background:radial-gradient(circle,rgba(211,165,207,.55) 0%,rgba(211,165,207,0) 70%)}

/* footer */
.site-footer{position:absolute;left:0;top:3405px;width:1200px;height:280px;background:linear-gradient(180deg,#e8dff0 0%,#e2d7ec 100%)}
.site-footer .brand{left:89px;top:100px;font-size:44px;gap:14px}
.site-footer .brand .dot{width:30px;height:30px}
.social{position:absolute;left:520px;top:105px;display:flex;gap:5px}
.social span{width:37px;height:37px;border-radius:50%;background:var(--ink)}
.foot-nav{position:absolute;left:815px;top:114px;display:flex;gap:28px;font-size:14px;color:var(--ink)}
.foot-rule{position:absolute;left:65px;top:229px;width:1070px;height:1px;background:#cbbfd6}
.copy{position:absolute;left:0;width:1200px;top:246px;text-align:center;font-size:13px;color:#444}
</style>
</head>
<body>

<header class="site-header">
  <div class="brand"><span class="dot"></span>velquogen</div>
  <nav class="main-nav">
    <svg class="home" viewBox="0 0 14 14"><path d="M1 7 7 1l6 6h-2v6H9V9H5v4H3V7z" fill="#a7469a"/></svg>
    <span>About</span><span>Technology</span><span>Contact</span>
  </nav>
  <a class="pill" style="left:931px;top:21px;width:180px;height:42px">
    <span style="width:148px">Get in Touch</span>
    <i style="width:42px;height:42px"><svg width="18" height="12" viewBox="0 0 18 12"><path d="M1 6h15M11 1l5 5-5 5" stroke="#fff" stroke-width="1.6" fill="none"/></svg></i>
  </a>
</header>

<section class="hero">
  <h1>Precision Immune<br>Targeting Starts Here</h1>
  <p>VELQUO — a rapid, versatile, and affordable platform to identify antigen-specific T cells for immunotherapy, autoimmunity, and beyond.</p>
  <a class="pill" style="left:113px;top:366px;width:284px;height:48px">
    <span style="width:240px">Learn How VELQUO Works</span>
    <i style="width:48px;height:48px"><svg width="18" height="12" viewBox="0 0 18 12"><path d="M1 6h15M11 1l5 5-5 5" stroke="#fff" stroke-width="1.6" fill="none"/></svg></i>
  </a>
  <div class="hero-art" role="img" aria-label="Molecular cluster artwork with microscopy imagery of immune cells"></div>
</section>

<section class="intro">
  <div class="plate"></div>
  <div class="photo" role="img" aria-label="Hand touching a holographic DNA interface"></div>
  <h2 class="intro-title">Introducing VELQUO</h2>
  <p class="intro-text">VELQUO is a proprietary platform designed to identify antigen-specific T cells — the immune system's most targeted weapons. Our method is rapid, unbiased, and cost-effective, enabling new insights into immune response across cancer, autoimmune, and infectious diseases.</p>
  <a class="pill" style="left:546px;top:370px;width:165px;height:40px">
    <span style="width:128px">Read More</span>
    <i style="width:40px;height:40px"><svg width="16" height="11" viewBox="0 0 18 12"><path d="M1 6h15M11 1l5 5-5 5" stroke="#fff" stroke-width="1.6" fill="none"/></svg></i>
  </a>

  <h2 class="how-title">How It Works</h2>
  <svg class="abs" style="left:0;top:0" width="1200" height="988" viewBox="0 0 1200 988">
    <g stroke="#d6d2d8" stroke-width="14" stroke-linecap="round">
      <line x1="232" y1="720" x2="478" y2="816"/>
      <line x1="478" y1="816" x2="723" y2="720"/>
      <line x1="723" y1="720" x2="969" y2="816"/>
    </g>
    <line x1="478" y1="719" x2="478" y2="790" stroke="#111" stroke-width="3"/>
    <g font-family="Sora, sans-serif" font-size="28" font-weight="600" fill="#fff" text-anchor="middle">
      <polygon points="232,684 317,720 232,756 147,720" fill="#6b3fa0"/>
      <text x="232" y="730">01</text>
      <polygon points="478,778 563,816 478,855 393,816" fill="#0b0b0b"/>
      <text x="478" y="826">02</text>
      <polygon points="723,684 808,720 723,756 638,720" fill="#6b3fa0"/>
      <text x="723" y="730">03</text>
      <polygon points="969,778 1054,816 969,855 884,816" fill="#6b3fa0"/>
      <text x="969" y="826">04</text>
    </g>
  </svg>
  <div class="step-label" style="left:358px;top:642px">Expose<small>to antigens</small></div>
  <div class="step-label" style="left:112px;top:779px">Isolate<small>immune cells</small></div>
  <div class="step-label" style="left:603px;top:779px">Detect<small>antigen-specific<br>T cells</small></div>
  <div class="step-label" style="left:849px;top:680px">Analyze<small>results using proprietary<br>algorithms</small></div>
</section>

<section class="about">
  <span class="tag">About</span>
  <h2>VELQUOgen</h2>
  <p class="lead">Founded by scientists and driven by innovation, VELQUOgen is advancing the future of immune diagnostics. Our mission is to accelerate the discovery of therapeutic T cells and support breakthroughs in personalized medicine.</p>
  <h3 style="left:89px;top:355px">Mission Statement</h3>
  <p class="mission">To make immune profiling faster, smarter, and accessible for everyone developing the next generation of therapies.</p>
  <h3 style="left:426px;top:355px">Core Values:</h3>
  <ul class="values">
    <li>Scientific Integrity</li>
    <li>Real-World Impact</li>
    <li>Speed &amp; Simplicity</li>
    <li>Collaboration</li>
  </ul>
  <div class="photo" role="img" aria-label="Scientist in a lab examining a sample dish beside a microscope"></div>
</section>

<section class="why">
  <h2>Why It's Different</h2>
  <div class="row" style="top:145px">
    <span class="mark"></span>
    <h3>01. Rapid</h3><div class="sub">Same-day insights</div>
    <div class="desc">It is a long established fact that a reader will be distracted by the readable content of a page when looking at its layout.</div>
    <span class="go"><svg width="20" height="14" viewBox="0 0 18 12"><path d="M1 6h15M11 1l5 5-5 5" stroke="#fff" stroke-width="1.6" fill="none"/></svg></span>
  </div>
  <div class="divider" style="top:301px"></div>
  <div class="row" style="top:307px">
    <span class="mark"></span>
    <h3>02. Unbiased</h3><div class="sub">No need predefined</div>
    <div class="desc">It is a long established fact that a reader will be distracted by the readable content of a page when looking at its layout.</div>
    <span class="go"><svg width="20" height="14" viewBox="0 0 18 12"><path d="M1 6h15M11 1l5 5-5 5" stroke="#fff" stroke-width="1.6" fill="none"/></svg></span>
  </div>
  <div class="row active" style="top:463px">
    <span class="mark"></span>
    <h3 style="top:34px">03. Versatile</h3><div class="sub" style="top:64px">Works across diseases and sample types</div>
    <div class="desc" style="top:35px">It is a long established fact that a reader will be distracted by the readable content of a page when looking at its layout.</div>
    <span class="go"><svg width="20" height="14" viewBox="0 0 18 12"><path d="M1 6h15M11 1l5 5-5 5" stroke="#111" stroke-width="1.6" fill="none"/></svg></span>
  </div>
  <div class="row" style="top:611px">
    <span class="mark"></span>
    <h3 style="top:36px">04. Affordable</h3><div class="sub" style="top:66px">Scales easily in both research and clinical use</div>
    <div class="desc" style="top:37px">It is a long established fact that a reader will be distracted by the readable content of a page when looking at its layout.</div>
    <span class="go"><svg width="20" height="14" viewBox="0 0 18 12"><path d="M1 6h15M11 1l5 5-5 5" stroke="#fff" stroke-width="1.6" fill="none"/></svg></span>
  </div>
</section>

<section class="connect">
  <div class="glow"></div>
  <h2>Let's Connect</h2>
  <p>Whether you're an investor, collaborator, or fellow innovator, we'd love</p>
</section>

<footer class="site-footer">
  <div class="brand"><span class="dot"></span>velquogen</div>
  <div class="social"><span></span><span></span><span></span><span></span></div>
  <nav class="foot-nav"><span>Home</span><span>About</span><span>Technology</span><span>Contact</span></nav>
  <div class="foot-rule"></div>
  <div class="copy">© Copyright 2025 VELQUOgen. All rights reserved.</div>
</footer>

</body>
</html>
```